Quorvane Capital Modern Business Card

We need a modern business card template designed for Quorvane Capital.
Quorvane Capital is a diversified global cryptocurrency investment fund.

The font under the logo: Hiragino Kaku Gothic Pro

Color Hexcode: Main colors white (ffffff) & teal (188383), we are open to adding #fcca46 as an accent

Target Market(s)

Accredited Investors, high net worth individuals and institutional investors

Industry/Entity Type

Investment

Contact Information for Business Card

Contact Information should contain
Name
main phone +1 720 555 0147
cell
email

Font styles to use
Sans Serif
Other font styles liked:
• Hiragino Kaku Gothic Pro

Requirements
Must have
• would like to have icons that identify the contact information
• include our website: www.quorvanecapital.example
• include our Tagline: Diversified Crypto Investment Funds
Nice to have
• Would like to have a simple back side with the logo (without the words) and plenty of space

```html
<!DOCTYPE html>
<html lang="en">
<head>
<meta charset="UTF-8">
<title>Quorvane Capital Business Card</title>
<link rel="stylesheet" href="https://fonts.googleapis.com/css2?family=Noto+Sans+JP:wght@400;500&family=Oswald:wght@500&family=Montserrat:wght@400;500&display=swap">
<style>
  :root {
    --bg: #161616;
    --card: #2a2a2a;
    --card-edge: #1f1f1f;
    --teal: #188383;
    --white: #ffffff;
    --muted: #e8e8e8;
  }
  * { box-sizing: border-box; margin: 0; padding: 0; }
  html, body { width: 1200px; height: 900px; overflow: hidden; }
  body {
    background: var(--bg);
    position: relative;
    font-family: "Montserrat", sans-serif;
  }
  .card {
    position: absolute;
    left: 260px;
    width: 680px;
    height: 388px;
    background: linear-gradient(135deg, var(--card-edge) 0%, var(--card) 100%);
    overflow: hidden;
  }
  .card::after {
    content: "";
    position: absolute;
    left: 0; right: 0; bottom: 0;
    height: 6px;
    background: var(--teal);
  }
  .card--front { top: 48px; }
  .card--back { top: 466px; }

  /* front */
  .brand {
    position: absolute;
    left: 0; right: 0; top: 0; bottom: 6px;
    display: flex;
    align-items: center;
    justify-content: center;
    gap: 16px;
  }
  .brand__mark {
    width: 22px; height: 22px;
    background: var(--teal);
  }
  .brand__name {
    font-family: "Noto Sans JP", sans-serif;
    font-weight: 400;
    font-size: 30px;
    letter-spacing: 2px;
    color: var(--white);
    text-transform: uppercase;
  }

  /* back */
  .person {
    position: absolute;
    right: 450px;
    top: 140px;
    text-align: right;
  }
  .person__name {
    font-family: "Oswald", sans-serif;
    font-weight: 500;
    font-size: 40px;
    line-height: 1;
    color: var(--teal);
    text-transform: uppercase;
    letter-spacing: 0.5px;
  }
  .person__role {
    margin-top: 10px;
    font-size: 17px;
    color: var(--muted);
    letter-spacing: 1px;
  }
  .divider {
    position: absolute;
    left: 250px;
    top: 136px;
    width: 2px;
    height: 92px;
    background: var(--teal);
  }
  .contacts {
    position: absolute;
    left: 274px;
    top: 138px;
    list-style: none;
  }
  .contacts__item {
    display: flex;
    align-items: center;
    gap: 14px;
    height: 24px;
    font-size: 17px;
    letter-spacing: 0.8px;
    color: var(--white);
  }
  .contacts__icon {
    width: 14px; height: 14px;
    flex: none;
    fill: none;
    stroke: var(--teal);
    stroke-width: 1.6;
  }
  .contacts__icon--solid { fill: var(--teal); stroke: none; }
  .tagline {
    position: absolute;
    left: 90px;
    bottom: 38px;
    font-size: 17px;
    font-weight: 500;
    letter-spacing: 1.6px;
    color: var(--white);
    text-transform: uppercase;
  }
</style>
</head>
<body>
  <section class="card card--front">
    <div class="brand">
      <span class="brand__mark"></span>
      <span class="brand__name">Quorvane Capital</span>
    </div>
  </section>

  <section class="card card--back">
    <div class="person">
      <h1 class="person__name">Darren Kolby</h1>
      <p class="person__role">Managing Director</p>
    </div>
    <div class="divider"></div>
    <ul class="contacts">
      <li class="contacts__item">
        <svg class="contacts__icon contacts__icon--solid" viewBox="0 0 16 16"><path d="M3.5 1.5l2.5 0 1 3.5-1.6 1.2a8 8 0 0 0 4.4 4.4L11 9l3.5 1v2.5c0 .8-.7 1.5-1.5 1.5C7 14 2 9 2 3c0-.8.7-1.5 1.5-1.5z"/></svg>
        <span>+1 720 555 0147</span>
      </li>
      <li class="contacts__item">
        <svg class="contacts__icon" viewBox="0 0 16 16"><rect x="4" y="1.5" width="8" height="13" rx="1.2"/><line x1="7" y1="12" x2="9" y2="12"/></svg>
        <span>+1 720 555 0147</span>
      </li>
      <li class="contacts__item">
        <svg class="contacts__icon contacts__icon--solid" viewBox="0 0 16 16"><path d="M1 3.5h14v9H1z M1.5 4l6.5 5 6.5-5" /><path d="M1 3.5l7 5.5 7-5.5z" fill="#2a2a2a"/></svg>
        <span>info@quorvanecapital.example</span>
      </li>
      <li class="contacts__item">
        <svg class="contacts__icon" viewBox="0 0 16 16"><circle cx="8" cy="8" r="6.3"/><ellipse cx="8" cy="8" rx="2.8" ry="6.3"/><line x1="1.7" y1="8" x2="14.3" y2="8"/><line x1="2.8" y1="4.6" x2="13.2" y2="4.6"/><line x1="2.8" y1="11.4" x2="13.2" y2="11.4"/></svg>
        <span>www.quorvanecapital.example</span>
      </li>
    </ul>
    <p class="tagline">Diversified Crypto Investment Funds</p>
  </section>
</body>
</html>
```